Need new label for my eczema cream. Pinegrove Soothe Sea Balm. PLS NOTHING LAME AND CLIP ART-ISH!

Think corvanta website meets eczema....our site is pinegrovesoothe.com ill attach our current logo.

```html
<!DOCTYPE html>
<html lang="en">
<head>
<meta charset="utf-8">
<title>Soothing Cream Label Variations</title>
<link rel="stylesheet" href="https://fonts.googleapis.com/css2?family=Archivo+Narrow:wght@700&family=Montserrat:wght@400;700&family=Architects+Daughter&display=swap">
<style>
  :root {
    --page: #ffffff;
    --ink-dark: #3c3c3e;
    --ink-soft: #4a4f55;

    --mist-bg: #dce7ef;
    --mist-wave: #cfdde8;
    --mist-head: #4b7fb5;
    --mist-herb: #b4bcc4;

    --sun-bg: #e4c92e;
    --sun-wave: #ead655;
    --sun-head: #3d3d3d;
    --sun-herb: #f6efbf;
    --sun-badge: #e8edf0;

    --frost-bg: #e7eef3;
    --frost-wave: #dbe6ee;
    --frost-head: #8eb0cd;
    --frost-herb: #c3ccd3;
    --frost-badge: #c7dbe8;
    --frost-badge-ink: #6f8699;

    --brand-yellow: #e4c72c;
  }

  * { box-sizing: border-box; margin: 0; padding: 0; }

  html, body {
    width: 1200px;
    height: 444px;
    overflow: hidden;
    background: var(--page);
  }

  .label-set {
    position: relative;
    width: 1200px;
    height: 444px;
    display: flex;
    gap: 25px;
    padding: 86px 50px;
  }

  .label {
    position: relative;
    width: 350px;
    height: 272px;
    overflow: hidden;
    background: var(--label-bg);
  }

  .label--mist  { --label-bg: var(--mist-bg);  --wave: var(--mist-wave);  --head: var(--mist-head);  --herb: var(--mist-herb);  --badge: var(--brand-yellow); --badge-ink: var(--ink-dark); }
  .label--sun   { --label-bg: var(--sun-bg);   --wave: var(--sun-wave);   --head: var(--sun-head);   --herb: var(--sun-herb);   --badge: var(--sun-badge);    --badge-ink: var(--ink-dark); }
  .label--frost { --label-bg: var(--frost-bg); --wave: var(--frost-wave); --head: var(--frost-head); --herb: var(--frost-herb); --badge: var(--frost-badge);  --badge-ink: var(--frost-badge-ink); }

  .label__wave-art {
    position: absolute;
    left: 90px;
    top: 40px;
    width: 280px;
    height: 200px;
    border-radius: 50% 50% 0 0;
    background: radial-gradient(ellipse at 55% 55%, var(--wave) 0%, var(--wave) 45%, transparent 72%);
  }

  .label__category {
    position: absolute;
    left: 23px;
    top: 34px;
    font-family: "Montserrat", sans-serif;
    font-weight: 400;
    font-size: 12px;
    letter-spacing: 3.2px;
    color: var(--ink-soft);
  }

  .label__title {
    position: absolute;
    left: 22px;
    top: 52px;
    font-family: "Archivo Narrow", sans-serif;
    font-weight: 700;
    font-size: 34px;
    line-height: 39px;
    color: var(--head);
    text-transform: uppercase;
    white-space: nowrap;
  }

  .label__ingredients {
    position: absolute;
    left: 23px;
    top: 150px;
    font-family: "Architects Daughter", cursive;
    font-size: 20px;
    line-height: 37px;
    color: var(--herb);
  }

  .label__volume {
    position: absolute;
    left: 26px;
    top: 240px;
    font-family: "Montserrat", sans-serif;
    font-weight: 700;
    font-size: 9.5px;
    color: var(--ink-dark);
  }

  .label__badge {
    position: absolute;
    left: 205px;
    top: 147px;
    width: 88px;
    height: 125px;
    border-radius: 44px 44px 0 0;
    background: var(--badge);
    display: flex;
    align-items: center;
    justify-content: center;
    padding-top: 24px;
  }

  .label__brand {
    font-family: "Archivo Narrow", sans-serif;
    font-weight: 700;
    font-size: 13px;
    line-height: 15px;
    text-align: center;
    text-transform: uppercase;
    color: var(--badge-ink);
  }
</style>
</head>
<body>
  <main class="label-set">

    <section class="label label--mist">
      <div class="label__wave-art" role="img" aria-label="Soft ocean wave illustration in pale blue"></div>
      <p class="label__category">SOOTHING CREAM</p>
      <h1 class="label__title">Pinegrove<br>Soothe Sea Balm</h1>
      <p class="label__ingredients">Sea Moss<br>Aloe Vera Oats</p>
      <p class="label__volume">4fl oz / 118 ml</p>
      <div class="label__badge"><span class="label__brand">Pinegrove<br>Soothe</span></div>
    </section>

    <section class="label label--sun">
      <div class="label__wave-art" role="img" aria-label="Line-drawn ocean wave illustration in white on yellow"></div>
      <p class="label__category">SOOTHING CREAM</p>
      <h2 class="label__title">Pinegrove<br>Soothe Sea Balm</h2>
      <p class="label__ingredients">Sea Moss<br>Aloe Vera Oats</p>
      <p class="label__volume">4fl oz / 118 ml</p>
      <div class="label__badge"><span class="label__brand">Pinegrove<br>Soothe</span></div>
    </section>

    <section class="label label--frost">
      <div class="label__wave-art" role="img" aria-label="Faint ocean wave illustration in pale blue-grey"></div>
      <p class="label__category">SOOTHING CREAM</p>
      <h2 class="label__title">Pinegrove<br>Soothe Sea Balm</h2>
      <p class="label__ingredients">Sea Moss<br>Aloe Vera Oats</p>
      <p class="label__volume">4fl oz / 118 ml</p>
      <div class="label__badge"><span class="label__brand">Pinegrove<br>Soothe</span></div>
    </section>

  </main>
</body>
</html>
```